Tot Petal Product Label for Tear-Free Head-to-Toe Wash

Need a bottle label design for a new line of natural products targeting infants and children. Products are Pediatrician-developed and paraben-free, sulfate-free, fragrance-free, and cruelty-free. Design should be clean and have a high-end feel to it. Will need other product labels in Tot Petal line designed as well in upcoming projects.

Target Market(s)

Newborn to young elementary age children and their parents

Industry/Entity Type

Cosmetics/Beauty

Font styles to use
Other font styles liked:
• Brand fonts are Jost and Sonorous

Colors

Designer to choose colors to be used in the design.

Requirements
Must have
• Tot Petal logo, Pediatrician Developed logo, and a clean high-end feel to it. The label must fit the specialty bottle we will be using (label measurements and diagram will be provided) for the front and back of bottle only (NOT the side labels). It must include our list of ingredients (will provide once designer selected).
Nice to have
• Should stand out on the shelf of other baby products due to it's clean simplicity and high-end feel
Should not have
• too much of a "kiddie" feel to it (targeting the parents not the kids)

```html
<!DOCTYPE html>
<html lang="en">
<head>
<meta charset="utf-8">
<title>Tot Petal – Tear-Free Head-to-Toe Wash Label</title>
<link href="https://fonts.googleapis.com/css2?family=Jost:wght@400;500&family=Varela+Round&display=swap" rel="stylesheet">
<style>
  :root {
    --canvas: #eef3f4;
    --label: #ffffff;
    --ink: #707070;
    --ink-soft: #8a8a8a;
    --brand: #7a6a55;
    --ring: #3a3a3a;
    --peach: #f6c8ae;
    --duck: #fbeb8a;
    --water: #8ccbee;
    --green: #8cc56a;
    --pink: #e86aa0;
    --orange: #f3b26a;
    --red: #ef8a6a;
    --teal: #6cc3c4;
  }
  * { margin: 0; padding: 0; box-sizing: border-box; }
  html, body { width: 1200px; height: 1200px; overflow: hidden; }
  body {
    background: var(--canvas);
    display: flex; align-items: center; justify-content: center;
    font-family: "Jost", sans-serif;
  }
  .label {
    position: relative;
    width: 780px; height: 1000px;
    background: var(--label);
    border-radius: 28px;
  }
  .brand-mark {
    position: absolute; left: 50%; top: 100px; transform: translateX(-50%);
    width: 208px; height: 208px; border-radius: 50%;
    border: 3px solid var(--ring);
    display: flex; align-items: center; justify-content: center;
  }
  .brand-name {
    font-family: "Jost", sans-serif; font-weight: 500;
    font-size: 26px; letter-spacing: 3px; color: var(--brand);
    text-transform: uppercase; white-space: nowrap;
  }
  .ped-badge {
    position: absolute; left: 572px; top: 150px;
    width: 90px; height: 90px; border-radius: 50%;
    border: 3px solid var(--teal);
  }
  .title {
    position: absolute; left: 0; right: 0; top: 345px;
    text-align: center; font-weight: 400;
    font-family: "Varela Round", sans-serif;
    color: var(--ink); font-size: 44px; line-height: 1.0;
  }
  .subtitle {
    position: absolute; left: 0; right: 0; top: 455px;
    text-align: center; font-size: 20px; letter-spacing: 3px; color: var(--ink-soft);
  }
  .illustration {
    position: absolute; left: 250px; top: 515px;
    width: 250px; height: 455px; border-radius: 40px;
    background: linear-gradient(180deg, var(--peach) 0%, var(--duck) 55%, var(--water) 100%);
    opacity: .85;
  }
  .claim {
    position: absolute; top: 765px;
    width: 80px; text-align: center; font-size: 12px; color: var(--ink-soft);
    white-space: nowrap;
  }
  .claim.paraben { left: 85px; }
  .claim.cruelty { left: 166px; }
  .claim.sulfate { left: 510px; }
  .claim.fragrance { left: 595px; }
  .claim-icon {
    width: 62px; height: 62px; margin: 0 auto 6px; border-radius: 50%;
    border: 3px solid currentColor; display: flex; align-items: center; justify-content: center;
  }
  .claim.paraben .claim-icon { color: var(--green); }
  .claim.cruelty .claim-icon { color: var(--pink); }
  .claim.sulfate .claim-icon { color: var(--orange); }
  .claim.fragrance .claim-icon { color: var(--red); }
</style>
</head>
<body>
  <main class="label">
    <div class="brand-mark"><span class="brand-name">Tot Petal</span></div>
    <div class="ped-badge" aria-hidden="true"></div>

    <h1 class="title">Tear-Free<br>Head-to-Toe Wash</h1>
    <p class="subtitle">Lavender &amp; Argan Oil</p>

    <div class="illustration" role="img" aria-label="Illustration of a yellow duckling holding a peach umbrella, splashing in water"></div>

    <div class="claim paraben">
      <div class="claim-icon">
        <svg width="30" height="30" viewBox="0 0 30 30"><path d="M15 26 C6 20 6 10 15 4 C24 10 24 20 15 26Z" fill="none" stroke="currentColor" stroke-width="2.5"/></svg>
      </div>Paraben-Free
    </div>
    <div class="claim cruelty">
      <div class="claim-icon">
        <svg width="30" height="30" viewBox="0 0 30 30"><path d="M15 25 L5 14 A5 5 0 0 1 15 8 A5 5 0 0 1 25 14Z" fill="currentColor"/></svg>
      </div>Cruelty-Free
    </div>
    <div class="claim sulfate">
      <div class="claim-icon">
        <svg width="30" height="30" viewBox="0 0 30 30"><path d="M11 4 H19 M13 4 V12 L6 25 H24 L17 12 V4" fill="none" stroke="currentColor" stroke-width="2.5" stroke-linejoin="round"/></svg>
      </div>Sulfate-Free
    </div>
    <div class="claim fragrance">
      <div class="claim-icon">
        <svg width="30" height="30" viewBox="0 0 30 30"><circle cx="15" cy="17" r="8" fill="none" stroke="currentColor" stroke-width="2.5"/><path d="M5 27 L25 5" stroke="currentColor" stroke-width="2.5"/></svg>
      </div>Fragrance-Free
    </div>
  </main>
</body>
</html>
```